Business card design needed

New company based in Brisbane, Australia. Brindle Systems. The business is focused on the delivery of network architecture design and deployment. We will provide both services and the sale of the necessary equipment to deliver the service. Cloud computing is an important element of our focus as this is an emerging market for enterprises in Queensland. Our target marketplace is medium to large corporations with complex infrastructure requirements. IT Management and above will be the typical entry point for us into these accounts. We would like to see the use of various shade of green, design should be clutter free and impress stability, trust and growth.
Updates
Hey Everyone
Just we let you all know we have changed this project to 'committed' payment status.
Looking forward to seeing the designs! Thanks for your efforts.
Best Regards
Marcus
Industry/Entity Type
Architecture
Contact Information for Business Card
Brindle Systems, Marcus Doyle, Sales Director, Level 14 Harlow Tower, 58 Penfold Street, Brisbane QLD 4000, Ph +61 7 3904 2267, M +61 4 4926 1573, E marcus.doyle@brindlesystems-example.com.au
Look and feel
Each slider illustrates characteristics of the customer's brand and the style your logo design should communicate.

```html
<!DOCTYPE html>
<html lang="en">
<head>
<meta charset="utf-8">
<title>Brindle Systems – Business Card</title>
<link rel="stylesheet" href="https://fonts.googleapis.com/css2?family=Tenor+Sans&family=Open+Sans:wght@400;600;700&display=swap">
<style>
  :root {
    --canvas: #e9e6e1;
    --green-deep: #003d1e;
    --green-band: #00512a;
    --green-stripe: #007a40;
    --ink: #111111;
    --paper: #ffffff;
    --url-tint: #cfe0d5;
  }
  * { box-sizing: border-box; margin: 0; padding: 0; }
  html, body { width: 1200px; height: 1000px; overflow: hidden; }
  body {
    background: var(--canvas);
    font-family: "Open Sans", sans-serif;
    position: relative;
  }
  .card {
    position: absolute;
    top: 350px;
    width: 540px;
    height: 302px;
    box-shadow: 0 6px 18px rgba(0,0,0,0.25);
    overflow: hidden;
  }
  .card-front { left: 46px; background: var(--paper); }
  .card-back { left: 614px; background: var(--green-deep); }

  .front-top-stripe { position: absolute; left: 0; top: 0; width: 100%; height: 12px; background: var(--green-stripe); }
  .brand-name {
    font-family: "Tenor Sans", sans-serif;
    color: var(--green-deep);
    white-space: nowrap;
  }
  .front-brand { position: absolute; left: 14px; top: 16px; font-size: 27px; }

  .person { position: absolute; left: 0; width: 100%; text-align: center; }
  .person-name { top: 90px; font-size: 21px; font-weight: 700; color: var(--ink); }
  .person-title { top: 118px; font-size: 18px; letter-spacing: 1.5px; color: var(--ink); }

  .contact-band { position: absolute; left: 0; top: 192px; width: 100%; height: 110px; background: var(--green-band); }
  .contact-band-edge { position: absolute; left: 0; width: 100%; background: var(--green-stripe); }
  .edge-top { top: 0; height: 10px; }
  .edge-bottom { bottom: 0; height: 12px; }

  .contact-line {
    position: absolute; color: var(--paper); font-size: 13px; white-space: nowrap;
    display: flex; align-items: center; gap: 8px;
  }
  .contact-line.right { right: 14px; justify-content: flex-end; text-align: right; }
  .contact-line.left { left: 12px; }
  .contact-icon { width: 18px; height: 18px; flex: none; }
  .address { line-height: 19px; }

  .back-rule {
    position: absolute; left: 70px; width: 400px; height: 2px;
    background: linear-gradient(90deg, rgba(255,255,255,0), rgba(255,255,255,0.9) 50%, rgba(255,255,255,0));
  }
  .back-rule.top { top: 64px; }
  .back-rule.bottom { top: 238px; }
  .back-brand {
    position: absolute; left: 0; top: 118px; width: 100%; text-align: center;
    font-size: 36px;
  }
  .back-brand .brand-name { color: var(--paper); }
  .back-url { position: absolute; left: 0; top: 162px; width: 100%; text-align: center; font-size: 13px; color: var(--url-tint); }
</style>
</head>
<body>
  <section class="card card-front" aria-label="Card front">
    <div class="front-top-stripe"></div>
    <div class="front-brand"><span class="brand-name">Brindle Systems</span></div>
    <div class="person person-name">Marcus Doyle</div>
    <div class="person person-title">sales director</div>

    <div class="contact-band">
      <div class="contact-band-edge edge-top"></div>
      <div class="contact-band-edge edge-bottom"></div>

      <div class="contact-line left" style="top:24px">
        <svg class="contact-icon" viewBox="0 0 18 18" aria-hidden="true"><circle cx="9" cy="9" r="8" fill="none" stroke="#fff" stroke-width="1.2"/><path d="M6 4.5c-1 .8-1.3 2-.6 3.5 1 2.2 2.6 3.8 4.6 4.8 1.4.7 2.5.4 3.3-.6l-1.6-1.5-1.2.8c-1.2-.6-2.2-1.6-2.8-2.8l.8-1.2z" fill="#fff"/></svg>
        <span>+61 7 3904 2267</span>
      </div>
      <div class="contact-line left" style="top:59px">
        <svg class="contact-icon" viewBox="0 0 18 18" aria-hidden="true"><circle cx="9" cy="9" r="8" fill="none" stroke="#fff" stroke-width="1.2"/><rect x="6" y="3.8" width="6" height="10.4" rx="1" fill="none" stroke="#fff" stroke-width="1.2"/><rect x="7.2" y="5.2" width="3.6" height="5" fill="#fff"/></svg>
        <span>+61 4 4926 1573</span>
      </div>

      <div class="contact-line right" style="top:24px">
        <span>marcus.doyle@brindlesystems-example.com.au</span>
        <svg class="contact-icon" viewBox="0 0 18 18" aria-hidden="true"><circle cx="9" cy="9" r="8" fill="none" stroke="#fff" stroke-width="1.2"/><rect x="4.5" y="6" width="9" height="6.2" fill="#fff"/><path d="M4.5 6l4.5 3.6L13.5 6" fill="none" stroke="#00512a" stroke-width="1"/></svg>
      </div>
      <div class="contact-line right" style="top:48px">
        <span class="address">Level 14 Harlow Tower, 58 Penfold Street,<br>Brisbane QLD 4000</span>
        <svg class="contact-icon" viewBox="0 0 18 18" aria-hidden="true" style="align-self:flex-end"><circle cx="9" cy="9" r="8" fill="none" stroke="#fff" stroke-width="1.2"/><path d="M4 9.2L9 4.8l5 4.4h-1.4v4.2H10.4V10.8H7.6v2.6H5.4V9.2z" fill="#fff"/></svg>
      </div>
    </div>
  </section>

  <section class="card card-back" aria-label="Card back">
    <div class="back-rule top"></div>
    <div class="back-brand"><span class="brand-name">Brindle Systems</span></div>
    <div class="back-url">brindlesystems-example.com.au</div>
    <div class="back-rule bottom"></div>
  </section>
</body>
</html>
```